A simple Chatterbook Ad (not Chatterbook Page) for weight loss surgery

It’s a simple ad in terms of the text.

The text should say:
Curious about weight loss surgery?
This 30 second quiz will tell you which procedure will suit you best

I'm open to variations in the text if it is thought to enhance the ad.

Targeted towards obese individuals who have been unable to lose weight with diet and exercise. My industry is weight loss surgery – webpage www.marcusbellweather.com.au. Clicking the ad leads to a quiz on my webpage relating to weight loss surgery. Most frequent users of this service are females (75%) between ages of 35 and 55 years.

Successful weight loss surgery can enable individuals who have been unable to lose weight to lose a substantial amount of the excess weight they are carrying to be healthier and happier.

```html
<!DOCTYPE html>
<html lang="en">
<head>
<meta charset="UTF-8">
<title>Marcus Bellweather – Weight Loss Surgery Quiz Ad</title>
<link href="https://fonts.googleapis.com/css2?family=Playfair+Display:wght@400&family=Jost:wght@300;400&display=swap" rel="stylesheet">
<style>
  :root {
    --navy-deep: #050c1c;
    --surgical-blue: #1f5fb8;
    --scrub-blue: #2a78c9;
    --panel-teal-top: rgba(14, 128, 132, 0.86);
    --panel-teal-bottom: rgba(52, 190, 180, 0.82);
    --brand-ink: #1a6f6a;
    --white: #ffffff;
    --button-grey: #474747;
  }
  * { margin: 0; padding: 0; box-sizing: border-box; }
  html, body {
    width: 1200px;
    height: 1200px;
    overflow: hidden;
    background: var(--navy-deep);
  }
  .ad {
    position: relative;
    width: 1200px;
    height: 1200px;
    overflow: hidden;
  }
  .surgery-photo {
    position: absolute;
    inset: 0;
    background:
      radial-gradient(ellipse 420px 380px at 330px 340px, rgba(120, 175, 230, 0.75), transparent 70%),
      radial-gradient(ellipse 500px 420px at 520px 1050px, rgba(40, 110, 200, 0.8), transparent 70%),
      radial-gradient(ellipse 260px 420px at 1150px 650px, rgba(45, 120, 210, 0.7), transparent 70%),
      radial-gradient(ellipse 340px 300px at 780px 330px, rgba(30, 60, 90, 0.6), transparent 70%),
      linear-gradient(160deg, var(--surgical-blue) 0%, var(--navy-deep) 45%, #0a1a3a 70%, var(--scrub-blue) 100%);
  }
  .brand-tab {
    position: absolute;
    top: 0;
    right: 0;
    width: 537px;
    height: 165px;
  }
  .brand-tab svg { position: absolute; inset: 0; }
  .brand {
    position: absolute;
    top: 48px;
    right: 24px;
    display: flex;
    align-items: center;
    gap: 14px;
  }
  .brand-dot {
    width: 30px;
    height: 30px;
    border-radius: 50%;
    background: var(--brand-ink);
    flex: none;
  }
  .brand-text { display: flex; flex-direction: column; }
  .brand-name {
    font-family: "Jost", sans-serif;
    font-weight: 400;
    font-size: 32px;
    line-height: 1.05;
    color: var(--brand-ink);
    white-space: nowrap;
  }
  .brand-role {
    margin-top: 4px;
    font-family: "Jost", sans-serif;
    font-weight: 400;
    font-size: 14px;
    line-height: 1.2;
    color: var(--brand-ink);
    white-space: nowrap;
  }
  .offer-panel {
    position: absolute;
    left: 52px;
    top: 497px;
    width: 993px;
    height: 538px;
    border-radius: 31px;
    background: linear-gradient(180deg, var(--panel-teal-top) 0%, var(--panel-teal-bottom) 100%);
  }
  .headline {
    position: absolute;
    left: 96px;
    top: 60px;
    font-family: "Playfair Display", serif;
    font-weight: 400;
    font-size: 86px;
    line-height: 96px;
    color: var(--white);
    letter-spacing: -0.5px;
    white-space: nowrap;
  }
  .subline {
    position: absolute;
    left: 95px;
    top: 270px;
    font-family: "Jost", sans-serif;
    font-weight: 300;
    font-size: 44px;
    line-height: 50px;
    color: var(--white);
    white-space: nowrap;
  }
  .cta-button {
    position: absolute;
    left: 95px;
    top: 410px;
    width: 250px;
    height: 55px;
    border-radius: 10px;
    background: var(--button-grey);
    color: var(--white);
    font-family: "Jost", sans-serif;
    font-weight: 300;
    font-size: 23px;
    display: flex;
    align-items: center;
    justify-content: center;
    text-decoration: none;
  }
</style>
</head>
<body>
  <main class="ad">
    <div class="surgery-photo" role="img" aria-label="Photograph of a surgical team in blue scrubs, caps and masks operating in a dim operating theatre with a monitor behind"></div>

    <header class="brand-tab">
      <svg width="537" height="165" viewBox="0 0 537 165" aria-hidden="true">
        <polygon points="0,0 537,0 537,165 89,165" fill="#ffffff"/>
      </svg>
      <div class="brand">
        <span class="brand-dot" aria-hidden="true"></span>
        <div class="brand-text">
          <span class="brand-name">Marcus Bellweather</span>
          <span class="brand-role">General, Upper GI &amp; Bariatric Surgeon</span>
        </div>
      </div>
    </header>

    <section class="offer-panel">
      <h1 class="headline">Curious about weight<br>loss surgery?</h1>
      <p class="subline">This 30 second quiz will tell you which<br>procedure will suit you best</p>
      <a class="cta-button" href="#">Get Started!</a>
    </section>
  </main>
</body>
</html>
```